Purchase Protection Subscription Program needs a refreshed website

We are refreshing an existing website www.buyguardian720.com. This is a purchase protection product which allows its members to receive extended warranty on the items they buy, receive a rebate of 50% on a repair of an item, a personal shopping concierge, etc. We are looking for a fresh, clean approach - with mass appeal to both men and woman. The site should convey trust, and ease of use.
Updates

Thanks to everyone who posted designs. Amazing work! It was a very difficult decision!

Industry/Entity Type

Product

```html
<!DOCTYPE html>
<html lang="en">
<head>
<meta charset="utf-8">
<title>BuyGuardian 720 – Purchase Protection</title>
<link rel="stylesheet" href="https://fonts.googleapis.com/css2?family=Open+Sans:ital,wght@0,400;0,600;0,700;1,400&display=swap">
<style>
:root{
  --teal:#4cc3a5;
  --ink:#1a1a1a;
  --muted:#8c8c8c;
  --light:#b3b3b3;
  --footer:#202020;
  --footer-field:#2e2e2e;
  --footer-text:#8a8a8a;
  --white:#ffffff;
}
*{margin:0;padding:0;box-sizing:border-box}
html,body{width:1147px;height:1200px;overflow:hidden;background:var(--white)}
body{position:relative;font-family:"Open Sans",Arial,sans-serif;color:var(--ink)}
a{color:inherit;text-decoration:none}
.abs{position:absolute}

.account-tab{left:792px;top:0;width:200px;height:25px;background:var(--teal);
  clip-path:polygon(0 100%,12% 0,100% 0,88% 100%);display:flex;align-items:center;justify-content:center;
  font-size:9.5px;color:var(--white);text-transform:uppercase}
.account-tab a{padding:0 14px}
.account-tab a+a{border-left:1px solid rgba(255,255,255,.45)}

.brand{left:154px;top:42px;font-size:18px;font-weight:400;letter-spacing:-.3px;color:var(--ink)}
.main-nav{right:154px;top:50px;display:flex;gap:21px;font-size:10.5px;font-weight:600;text-transform:uppercase;color:var(--ink)}

.hero{left:174px;top:112px;width:790px;height:336px;
  background:linear-gradient(90deg,#e8402c 0%,#f39a2a 22%,#e8c26a 33%,#d9a57a 45%,#c9764f 58%,#f2dc7a 72%,#f69a5c 85%,#f7f3ee 100%);}
.hero::after{content:"";position:absolute;left:0;right:0;bottom:0;height:70px;background:linear-gradient(rgba(255,255,255,0),rgba(255,255,255,.85))}
.hero-title{left:232px;top:228px;font-size:30px;font-weight:700;color:var(--white);text-shadow:0 2px 6px rgba(0,0,0,.35)}
.hero-sub{left:232px;top:270px;font-size:17.5px;font-weight:700;color:var(--white);text-shadow:0 1px 4px rgba(0,0,0,.35)}
.hero-sub mark{background:var(--teal);color:var(--white);padding:0 3px}
.slider-arrow{top:265px;width:26px;height:26px;border:1.5px solid rgba(255,255,255,.8);border-radius:50%}
.slider-dots{left:546px;top:426px;display:flex;gap:9px}
.slider-dots span{width:12px;height:12px;border:1.5px solid rgba(255,255,255,.9);border-radius:50%}
.slider-dots span.active{background:rgba(255,255,255,.9)}

.feature{top:534px;height:260px;text-align:center}
.feature-icon{width:92px;height:92px;margin:0 auto;border-radius:50%;background:var(--teal);display:flex;align-items:center;justify-content:center}
.feature-title{margin-top:19px;font-size:13.5px;font-weight:600;line-height:18px}
.feature-text{margin-top:11px;font-size:10.4px;line-height:17.2px;color:var(--muted)}
.feature-list{margin-top:7px;color:var(--teal)}
.hl{color:var(--teal)}
.feature-plus{font-size:13px;color:var(--teal)}
.btn{position:absolute;left:50%;top:233px;transform:translateX(-50%);width:72px;height:25px;background:var(--ink);color:var(--white);font-size:10.4px;line-height:25px}

.disclaimer{left:172px;top:858px;width:804px;text-align:center;font-size:8px;font-style:italic;line-height:17.2px;color:var(--light)}

.site-footer{left:0;top:1006px;width:1147px;height:194px;background:var(--footer);color:var(--footer-text)}
.footer-heading{top:40px;font-size:12px;font-weight:400;color:var(--white)}
.footer-about{left:154px;top:69px;width:196px;font-size:9.5px;line-height:17.2px}
.footer-links{top:72px;font-size:9px;line-height:15px;text-transform:uppercase}
.social{left:584px;top:67px;display:flex;gap:14px}
.social span{width:22px;height:22px;border:1.5px solid var(--footer-text);border-radius:50%}
.subscribe-input{left:800px;top:67px;width:128px;height:21px;background:var(--footer-field);border:0;font:8.5px "Open Sans",sans-serif;color:var(--footer-text);padding-left:7px}
.subscribe-btn{left:939px;top:67px;width:24px;height:21px;background:var(--footer-field);font-size:8.5px;line-height:21px;text-align:center}
.copyright{left:154px;top:170px;font-size:8.5px}
</style>
</head>
<body>

<nav class="abs account-tab"><a href="#">My Account</a><a href="#">Login</a></nav>
<div class="abs brand">BuyGuardian 720</div>
<nav class="abs main-nav">
  <a href="#">Home</a><a href="#">About Us</a><a href="#">Privacy</a><a href="#">Product Features</a><a href="#">How It Works</a><a href="#">Contact Us</a>
</nav>

<div class="abs hero" role="img" aria-label="Smiling shopper lying on the floor with a laptop, surrounded by colourful shopping bags and wrapped gifts"></div>
<h1 class="abs hero-title">Shop with confidence</h1>
<p class="abs hero-sub">knowing <mark>BuyGuardian 720</mark> is there...</p>
<span class="abs slider-arrow" style="left:183px"></span>
<span class="abs slider-arrow" style="left:938px"></span>
<div class="abs slider-dots"><span class="active"></span><span></span><span></span></div>

<section class="abs feature" style="left:151px;width:270px">
  <div class="feature-icon">
    <svg width="42" height="42" viewBox="0 0 42 42" fill="none" stroke="#fff" stroke-width="2.4">
      <path d="M23 5 L35 10 V20 C35 28 29 34 23 37 C17 34 11 28 11 20 V10 Z"/>
      <text x="23" y="26" text-anchor="middle" font-family="Open Sans,sans-serif" font-size="14" font-weight="700" fill="#fff" stroke="none">$</text>
      <path d="M3 27h8M3 31h9M3 35h11" stroke-width="2"/>
    </svg>
  </div>
  <h2 class="feature-title">Valuable Purchase Protection</h2>
  <p class="feature-text">Get 5 unique ways to get more out of the things you buy:</p>
  <p class="feature-text feature-list">Warranty Extension, Repair Bill Rebate<br>Product Return Guarantee, Price Protection<br>Restocking fee reimbursement</p>
  <a class="btn" href="#">Learn More</a>
</section>

<section class="abs feature" style="left:445px;width:256px">
  <div class="feature-icon">
    <svg width="34" height="38" viewBox="0 0 34 38" fill="none" stroke="#fff" stroke-width="2.4">
      <rect x="4" y="2" width="24" height="30"/>
      <path d="M8 36h22V8"/>
      <path d="M9 9h14M9 14h14M9 19h14M9 24h14" stroke-width="2"/>
    </svg>
  </div>
  <h2 class="feature-title">Easy Claims Process</h2>
  <p class="feature-text">Using <span class="hl">BuyGuardian 720</span> has never been easier. Just send us copies, scans or photos of your receipts -- we'll store them securely online. Then download what you need and submit your claim online.</p>
  <a class="btn" href="#">Learn More</a>
</section>

<section class="abs feature" style="left:745px;width:230px">
  <div class="feature-icon">
    <svg width="48" height="40" viewBox="0 0 48 40" fill="#fff">
      <ellipse cx="23" cy="25" rx="17" ry="11"/>
      <rect x="10" y="30" width="6" height="9" rx="2"/>
      <rect x="28" y="30" width="6" height="9" rx="2"/>
      <path d="M38 21l6-2v8l-5 1z"/>
      <circle cx="26" cy="8" r="7"/>
      <text x="26" y="12" text-anchor="middle" font-family="Open Sans,sans-serif" font-size="10" font-weight="700" fill="#4cc3a5">$</text>
    </svg>
  </div>
  <h2 class="feature-title">One low monthly fee</h2>
  <p class="feature-text" style="margin-top:9px"><span class="feature-plus">PLUS</span><br>Get a <span class="hl">$5 bonus</span><br><span class="hl">Rebate</span> each calendar quarter to use on home electronics &amp; appliance purchases!*</p>
  <a class="btn" href="#">Learn More</a>
</section>

<p class="abs disclaimer">*Exclusions and limitations apply. See Terms and Conditions for complete product benefit details. Warranty Extension and Repair Bill Rebate benefits are not available in Maine. Warranty Extension and Repair Bill Rebate benefits are provided by Northline Product Care Company, except in Arizona, Florida, Oklahoma and Wisconsin, where they are provided by Keystone Care Services, Incorporated (FL License Number 90412), both of which are located at 480 Meridian Ave., Springfield, IL 62701, (555) 014-2200. The programs are administered by Harbor Plan Solutions, Inc., 480 Meridian Ave., Springfield, IL 62701, (555) 014-2200. Bonus Rebates are limited to one rebate per purchased item and one purchase per calendar quarter.</p>

<footer class="abs site-footer">
  <h3 class="abs footer-heading" style="left:154px">About BuyGuardian 720</h3>
  <p class="abs footer-about">Lorem ipsum dolor sit amet, consectetur adipiscing elit. Aenean pharetra elit in nulla commodo, lobortis pretium nulla porta. Curabitur vitae purus ullamcorper, sodales odio eget, ultricies risus.</p>

  <h3 class="abs footer-heading" style="left:369px">Useful Links</h3>
  <div class="abs footer-links" style="left:369px"><a href="#">Home</a><br><a href="#">About Us</a><br><a href="#">Privacy</a></div>
  <div class="abs footer-links" style="left:458px"><a href="#">Product Features</a><br><a href="#">How It Works</a><br><a href="#">Contact Us</a></div>

  <h3 class="abs footer-heading" style="left:584px">Find Us:</h3>
  <div class="abs social"><span></span><span></span><span></span><span></span></div>

  <h3 class="abs footer-heading" style="left:800px">Join Mailing List:</h3>
  <input class="abs subscribe-input" type="email" placeholder="Email Adress...">
  <span class="abs subscribe-btn">OK</span>

  <p class="abs copyright">Copyright © 2014 BuyGuardian 720. All Rights Reserved.</p>
</footer>

</body>
</html>
```